QMCARGO FLYER

I would like a flyer to put out around town to advertise our business, (freight forwarding) i have a logo and i was also hoping we could have the reverse of the flyer in arabic, as alot of my clientele are from the Middle East. Photos could also be available?
Would like to have special offers to main destinations, i.e. Riyadh £2.50* All In
Jeddah £2.50* " "
Dubai""""""""""""""
Abu Dhabi"""""""""
Doha""""""""""""""
And some other major country (capitals) all the same price *subject to requirements

Airfreight / Sea freight
Airport Transport Services
Customs Clearance
Car Shipping
Packaging Material

contact details: Email: qmcargo@postvale.net
Tel: +44 (0) 20 7413 5961
Mob:+44 (0) 7392 816 054

Target Market(s)

Middle East
Arabic

Requirements
Must have
• Stand Out and be clear and not too cluttered.
• Want to get across exactly whats on offer.
• Reverse Mirrored in Arabic

```html
<!DOCTYPE html>
<html lang="en">
<head>
<meta charset="utf-8">
<title>QMCARGO Flyer</title>
<link rel="stylesheet" href="https://fonts.googleapis.com/css2?family=Mulish:wght@400;600;700;800&family=Tajawal:wght@400;500;700&display=swap">
<style>
  :root {
    --navy: #1c1e52;
    --navy-deep: #14163f;
    --white: #ffffff;
    --ink: #111111;
    --sky-top: #8d96c9;
    --sky-mid: #5d68a8;
    --sky-low: #2e3776;
    --city-top: #8a93c4;
    --city-low: #1e2758;
    --photo-sky: #7f8fb1;
    --photo-ground: #5a5c66;
  }
  * { box-sizing: border-box; margin: 0; padding: 0; }
  html, body { width: 865px; height: 1200px; overflow: hidden; background: var(--white); }
  .flyer {
    position: relative; width: 865px; height: 1200px;
    background: var(--white); font-family: "Mulish", sans-serif; overflow: hidden;
  }
  .top-band { position: absolute; left: 0; top: 0; width: 865px; height: 44px; background: var(--navy); }
  .photo {
    position: absolute; top: 55px; height: 141px;
    background: linear-gradient(180deg, var(--photo-sky) 0%, #9aa6c0 50%, var(--photo-ground) 72%, #3d3f47 100%);
  }
  .photo--plane { left: 0; width: 282px; }
  .photo--vans { left: 293px; width: 278px; }
  .photo--loading { left: 582px; width: 283px; }
  .photo-divider { position: absolute; left: 283px; top: 44px; width: 10px; height: 164px; background: var(--ink); }

  .services {
    position: absolute; left: 0; top: 207px; width: 865px; height: 295px; background: var(--navy);
    color: var(--white);
  }
  .services-list { position: absolute; left: 42px; top: 58px; list-style: none; }
  .services-list li { font-size: 23px; font-weight: 700; letter-spacing: 0.3px; height: 37.4px; line-height: 37px; }
  .services-list-ar {
    position: absolute; right: 22px; top: 56px; list-style: none; direction: rtl; text-align: right;
    font-family: "Tajawal", sans-serif;
  }
  .services-list-ar li { font-size: 27px; font-weight: 500; height: 37.4px; line-height: 37px; }

  .offers {
    position: absolute; left: 0; top: 505px; width: 865px; height: 240px;
    background: radial-gradient(ellipse at 48% 30%, #a3acd8 0%, transparent 45%),
                linear-gradient(180deg, var(--sky-top) 0%, var(--sky-mid) 55%, var(--sky-low) 100%);
  }
  .offers-text {
    position: absolute; left: 42px; top: 26px; color: var(--white);
    font-size: 17.5px; font-weight: 700; line-height: 21.5px;
  }
  .offers-text .gap { height: 21.5px; }

  .offers-ar {
    position: absolute; left: 0; top: 750px; width: 865px; height: 258px;
    background: linear-gradient(180deg, var(--city-top) 0%, #6e7ab4 35%, #3d4888 70%, var(--city-low) 100%);
  }
  .offers-ar-text {
    position: absolute; right: 46px; top: 20px; direction: rtl; text-align: right;
    color: var(--white); font-family: "Tajawal", sans-serif; font-size: 20px; font-weight: 500; line-height: 24px;
  }
  .offers-ar-text .gap { height: 24px; }

  .contact { position: absolute; left: 0; top: 1015px; width: 865px; height: 118px; background: var(--white); color: var(--ink); }
  .contact-en { position: absolute; left: 40px; top: 22px; font-size: 14px; font-weight: 800; line-height: 32px; }
  .contact-ar {
    position: absolute; right: 40px; top: 22px; direction: rtl; text-align: right;
    font-family: "Tajawal", sans-serif; font-size: 14px; font-weight: 700; line-height: 32px;
  }
  .contact-ar bdi { font-family: "Mulish", sans-serif; font-weight: 800; }
  .brand {
    position: absolute; left: 348px; top: 22px; width: 168px; height: 76px;
    display: flex; align-items: center; justify-content: center; gap: 8px;
  }
  .brand-dot { width: 14px; height: 14px; border-radius: 50%; background: var(--ink); }
  .brand-name { font-size: 24px; font-weight: 800; color: var(--ink); letter-spacing: 0.5px; }

  .bottom-line { position: absolute; left: 0; top: 1140px; width: 865px; height: 6px; background: var(--navy); }
  .bottom-band { position: absolute; left: 0; top: 1151px; width: 865px; height: 49px; background: var(--navy); }
</style>
</head>
<body>
<main class="flyer">
  <div class="top-band"></div>

  <div class="photo photo--plane" role="img" aria-label="Cargo airliner being loaded on an airport apron at dusk"></div>
  <div class="photo-divider"></div>
  <div class="photo photo--vans" role="img" aria-label="Row of white company delivery vans parked at an airport cargo area"></div>
  <div class="photo photo--loading" role="img" aria-label="Company van beside an airliner with cargo trolleys on the tarmac"></div>

  <section class="services">
    <ul class="services-list">
      <li>- Airfreight / Sea freight</li>
      <li>- Airport Transport Services</li>
      <li>- Customs Clearance</li>
      <li>- Car Shipping</li>
      <li>- Packaging Material</li>
    </ul>
    <ul class="services-list-ar" lang="ar">
      <li>- الشحن الجوي / الشحن البحري</li>
      <li>- مطار خدمات النقل</li>
      <li>- التخليص الجمركي</li>
      <li>- سيارة شحن</li>
      <li>- مواد التعبئة والتغليف</li>
    </ul>
  </section>

  <section class="offers" role="img" aria-label="Blue-toned view of a tall skyscraper against the sky">
    <div class="offers-text">
      <p>Would like to have special offers to main destinations,</p>
      <p>i.e. Riyadh £2.50* All In Jeddah £2.50* " "</p>
      <div class="gap"></div>
      <p>Dubai""""""""""""""</p>
      <p>Abu Dhabi"""""""""</p>
      <p>Doha""""""""""""""</p>
      <p>And some other major country (capitals) all the same price</p>
      <p>*subject to requirements</p>
    </div>
  </section>

  <section class="offers-ar" role="img" aria-label="Blue-toned night skyline of a city with illuminated towers">
    <div class="offers-ar-text" lang="ar">
      <p>،ترغب في الحصول على العروض الخاصة إلى وجهات رئيسية</p>
      <p>أي الرياض £ 2.50 * في كل وجدة £ 2.50* ""</p>
      <div class="gap"></div>
      <p>دبي"" "" "" "" "" "" ""</p>
      <p>أبوظبي"" "" "" "" ""</p>
      <p>الدوحة"" "" "" "" "" ""</p>
      <p>وبعض البلاد الرئيسية الأخرى (عواصم) كل نفس السعر</p>
      <p>تخضع لمتطلبات *</p>
    </div>
  </section>

  <footer class="contact">
    <div class="contact-en">
      <p>contact details: Email: qmcargo@postvale.net</p>
      <p>Tel: +44 (0) 20 7413 5961</p>
      <p>Mob:+44 (0) 7392 816 054</p>
    </div>
    <div class="brand">
      <span class="brand-dot"></span>
      <span class="brand-name">QMCARGO</span>
    </div>
    <div class="contact-ar" lang="ar">
      <p>تفاصيل الاتصال: البريد الإلكتروني: <bdi>qmcargo@postvale.net</bdi></p>
      <p>هاتف: <bdi>+44 (0) 20 7413 5961</bdi></p>
      <p>الجوال: <bdi>+44 (0) 7392 816 054</bdi></p>
    </div>
  </footer>

  <div class="bottom-line"></div>
  <div class="bottom-band"></div>
</main>
</body>
</html>
```